Tallow Quarry Gaming Website eSports

We need a website design for an eSports shop that we are opening. we have a logo that we will upload and would like the website to match the colours in the logo if possible. The website must have a strong gaming emphasis as this is a big part of our shop. we would also like some way of displaying leaderboards for tournaments that have been played if that can be done? also a pricing option and membership option displayed on the site with a contact form and opening hours. we have the domain name already. Any help would be great we just want a fun one page website if possible that people don't find hard to use. if you need anymore info or have any questions just ask

Target Market(s)

Gamers, Internet cafe,

Industry/Entity Type

Games

Coding

Coded - Design and coding required

Number of Pages Required

3 page

Requirements
Must have
• HTML, Contact Form, Responsive, Blog, Contact Us, add upcoming events, Links to social media
Nice to have
• The option to show a leaderboard of the top 5 places in tournaments that have been played

```html
<!DOCTYPE html>
<html lang="en">
<head>
<meta charset="utf-8">
<title>Tallow Quarry — eSports Arena</title>
<link rel="stylesheet" href="https://fonts.googleapis.com/css2?family=Exo+2:wght@300;400;500;600;700&family=Mulish:wght@400;600;700&display=swap">
<style>
:root{
  --ink:#241d6b;
  --navy:#17113f;
  --deep:#120c35;
  --royal:#2a43c4;
  --violet:#5a22d8;
  --purple:#7a2fd6;
  --lavender:#e4ddf3;
  --white:#ffffff;
  --line:#c9c6dc;
  --text:#2b2b3a;
  --pale:#d7d3f2;
}
*{box-sizing:border-box;margin:0;padding:0}
html,body{width:1200px;height:4717px;overflow:hidden}
body{position:relative;background:var(--white);font-family:"Mulish",sans-serif;color:var(--text)}
.abs{position:absolute}
.heading{font-family:"Exo 2",sans-serif;font-weight:600;letter-spacing:.5px}
.btn-outline{position:absolute;display:flex;align-items:center;justify-content:center;border:2px solid var(--ink);color:var(--ink);font-family:"Exo 2",sans-serif;font-weight:600;font-size:15px;letter-spacing:.5px;text-decoration:none}
.btn-outline.light{border-color:var(--white);color:var(--white)}

/* header */
.site-header{position:absolute;left:0;top:0;width:1200px;height:95px;background:var(--white);z-index:5}
.nav-link{position:absolute;top:44px;font-family:"Exo 2",sans-serif;font-weight:600;font-size:15px;color:var(--ink);text-decoration:none}
.nav-link.active{color:var(--purple)}
.brand-tab{position:absolute;left:0;top:0;z-index:6}
.brand-name{position:absolute;left:0;width:1200px;top:100px;text-align:center;font-family:"Exo 2",sans-serif;font-weight:600;font-size:25px;letter-spacing:2px;color:var(--ink);z-index:7}
.brand-dot{position:absolute;left:578px;top:18px;width:44px;height:44px;border-radius:50%;background:var(--ink);z-index:7}
.login-btn{left:934px;top:27px;width:176px;height:44px;font-size:13px}

/* hero */
.hero-art{position:absolute;left:0;top:95px;width:1200px;height:634px;background:
  radial-gradient(ellipse 420px 160px at 600px 500px,rgba(70,190,255,.45),transparent 70%),
  radial-gradient(ellipse 700px 420px at 600px 330px,#3a2a8f,transparent 75%),
  linear-gradient(90deg,#160e3c 0%,#2a1f6e 35%,#2b2c8a 55%,#3a1668 100%)}
.hero-kicker{position:absolute;left:0;width:1200px;top:300px;text-align:center;font-family:"Exo 2",sans-serif;font-weight:300;font-size:42px;color:var(--white);letter-spacing:1px}
.hero-title{position:absolute;left:0;width:1200px;top:338px;text-align:center;font-family:"Exo 2",sans-serif;font-weight:700;font-size:62px;color:var(--white);letter-spacing:1px}
.hero-btn{left:513px;top:425px;width:198px;height:48px;font-size:18px}
.arrow{position:absolute}

.soft-band{position:absolute;left:0;top:729px;width:1200px;height:700px;background:linear-gradient(180deg,var(--lavender),#fff 70%)}

/* feature diamonds */
.feature{position:absolute;text-align:center;color:var(--white)}
.feature h3{font-family:"Exo 2",sans-serif;font-weight:600;font-size:22px;letter-spacing:.5px}
.feature p{font-size:13px;line-height:20px;color:#dcd8ff;margin-top:6px}
.feature .chev{margin:14px auto 0;width:36px;height:36px;border:2px solid var(--white);border-radius:50%;display:flex;align-items:center;justify-content:center}

/* about */
.photo{position:absolute}
.section-title{font-family:"Exo 2",sans-serif;font-weight:600;font-size:33px;color:var(--ink)}
.body-copy{font-size:15.5px;line-height:25.5px;color:var(--text)}

/* tournaments */
.leader-row{position:absolute;left:222px;width:754px;height:60px;border:1px solid rgba(120,140,255,.7);background:linear-gradient(90deg,rgba(40,70,210,.9),rgba(40,50,170,.55));display:flex;align-items:center;color:var(--white)}
.leader-row .rank{width:58px;padding-left:24px;font-family:"Exo 2",sans-serif;font-weight:700;font-size:26px}
.leader-row .game{flex:1;padding-left:30px;font-family:"Exo 2",sans-serif;font-weight:600;font-size:19px;letter-spacing:.5px}
.leader-row .score{position:relative;width:136px;height:42px;display:flex;align-items:center;justify-content:center;font-family:"Exo 2",sans-serif;font-weight:600;font-size:19px;gap:8px}
.leader-row .score svg.frame{position:absolute;left:0;top:0}
.leader-row .go{width:58px;display:flex;justify-content:center}

/* games */
.game-cover{position:absolute;width:206px;height:206px;border-radius:50%;border:3px solid #e8e6f2}

/* pricing */
.plan{position:absolute;top:2570px;width:280px;height:416px;border:1px solid #3c3aa8;background:rgba(18,14,60,.85);color:var(--white)}
.plan-head{position:absolute;left:0;top:0;width:280px;height:130px}
.plan-name{position:absolute;left:0;width:278px;top:22px;text-align:center;font-family:"Exo 2",sans-serif;font-weight:500;font-size:23px}
.plan-price{position:absolute;left:0;width:278px;top:52px;text-align:center;font-family:"Exo 2",sans-serif;font-weight:500;font-size:22px}
.plan-price b{font-size:32px;font-weight:700}
.plan-desc{position:absolute;left:40px;width:210px;top:155px;font-size:12px;line-height:16.5px;color:#d9d6f2}
.plan-list{position:absolute;left:38px;top:220px;list-style:none}
.plan-list li{display:flex;align-items:center;gap:9px;height:32.5px;font-size:14px;color:#e4e1fa}
.plan-btn{left:26px;top:357px;width:228px;height:42px;font-size:15px}

/* contact */
.field{position:absolute;border:1px solid var(--line);background:#fff;font-size:13px;color:#555;padding:12px 16px}
.submit{left:502px;top:4320px;width:192px;height:53px;font-size:19px;border-width:3px;color:#2b3bb8;border-color:#2b3bb8}

/* footer */
.hours{position:absolute;left:0;width:1200px;top:4530px;text-align:center;font-family:"Exo 2",sans-serif;font-size:17px;color:#e7e4ff}
.foot-nav{position:absolute;left:0;width:1200px;top:4576px;display:flex;justify-content:center;gap:0}
.foot-nav a{font-family:"Exo 2",sans-serif;font-weight:600;font-size:15px;color:var(--white);text-decoration:none}
.copyright{position:absolute;left:0;width:1200px;top:4606px;text-align:center;font-size:11px;color:#cfcbee}
.social{position:absolute;top:4639px;width:44px;height:44px;border-radius:50%;background:#7b3fcf}
</style>
</head>
<body>

<!-- page background bands -->
<div class="hero-art" role="img" aria-label="Dark futuristic arena scene with a glowing blue stage"></div>
<div class="soft-band"></div>

<svg class="abs" style="left:0;top:0" width="1200" height="4717" viewBox="0 0 1200 4717">
  <defs>
    <linearGradient id="tourneyFill" x1="0" y1="0" x2="1" y2="1">
      <stop offset="0" stop-color="#1f3fc0"/>
      <stop offset=".55" stop-color="#2a35b0"/>
      <stop offset="1" stop-color="#3d1f9e"/>
    </linearGradient>
    <linearGradient id="pricingFill" x1="0" y1="0" x2="0" y2="1">
      <stop offset="0" stop-color="#1a1350"/>
      <stop offset=".5" stop-color="#221a63"/>
      <stop offset="1" stop-color="#150f40"/>
    </linearGradient>
    <linearGradient id="prizeFill" x1="0" y1="0" x2="1" y2="1">
      <stop offset="0" stop-color="#1b1350"/>
      <stop offset=".6" stop-color="#2a176e"/>
      <stop offset="1" stop-color="#3b1a80"/>
    </linearGradient>
    <linearGradient id="gamesFill" x1="0" y1="0" x2="0" y2="1">
      <stop offset="0" stop-color="#ffffff"/>
      <stop offset="1" stop-color="#ebe7f6"/>
    </linearGradient>
  </defs>
  <path d="M0 1374 Q600 1470 1200 1374 V2000 H0Z" fill="url(#tourneyFill)"/>
  <rect x="0" y="2000" width="1200" height="380" fill="url(#gamesFill)"/>
  <path d="M0 2354 Q600 2440 1200 2354 V3114 Q600 3010 0 3114Z" fill="url(#pricingFill)"/>
  <path d="M0 3410 Q600 3510 1200 3410 V4021 H0Z" fill="url(#prizeFill)"/>
  <path d="M0 4397 Q600 4475 1200 4397 V4717 H0Z" fill="#1d1552"/>
</svg>

<!-- header -->
<header class="site-header">
  <a class="nav-link active" style="left:114px" href="#">HOME</a>
  <a class="nav-link" style="left:190px" href="#">ABOUT</a>
  <a class="nav-link" style="left:273px" href="#">GAMES</a>
  <a class="nav-link" style="left:357px" href="#">EVENTS</a>
  <a class="nav-link" style="left:763px" href="#">PRICE</a>
  <a class="nav-link" style="left:838px" href="#">CONTACT</a>
  <a class="btn-outline login-btn" href="#">MEMBERSHIP LOGIN</a>
</header>
<svg class="brand-tab" width="1200" height="150" viewBox="0 0 1200 150">
  <path d="M430 94 L780 94 L752 143 L458 143Z" fill="#fff"/>
</svg>
<div class="brand-dot"></div>
<div class="brand-name">TALLOW QUARRY</div>

<!-- hero -->
<div class="hero-kicker">WELCOME TO</div>
<div class="hero-title">TALLOW QUARRY</div>
<a class="btn-outline light hero-btn" href="#">VIEW GAMES</a>
<svg class="arrow" style="left:104px;top:358px" width="26" height="50" viewBox="0 0 26 50"><path d="M24 2 L3 25 L24 48" fill="none" stroke="#fff" stroke-width="2.5"/></svg>
<svg class="arrow" style="left:1070px;top:358px" width="26" height="50" viewBox="0 0 26 50"><path d="M2 2 L23 25 L2 48" fill="none" stroke="#fff" stroke-width="2.5"/></svg>

<!-- feature diamonds -->
<svg class="abs" style="left:0;top:500px" width="1200" height="460" viewBox="0 500 1200 460">
  <defs>
    <linearGradient id="diaBlue" x1="0" y1="0" x2="0" y2="1">
      <stop offset="0" stop-color="#2552c8"/><stop offset="1" stop-color="#1a2fa6"/>
    </linearGradient>
    <linearGradient id="diaViolet" x1="0" y1="0" x2="0" y2="1">
      <stop offset="0" stop-color="#6a3fd0"/><stop offset="1" stop-color="#3a1fa0"/>
    </linearGradient>
  </defs>
  <polygon points="293,548 475,730 293,912 111,730" fill="url(#diaBlue)"/>
  <polygon points="920,548 1102,730 920,912 738,730" fill="url(#diaBlue)"/>
  <polygon points="614,528 816,730 614,932 412,730" fill="url(#diaViolet)" stroke="#8b7be0" stroke-width="3"/>
  <!-- crossed swords -->
  <g stroke="#fff" stroke-width="3" fill="none" stroke-linecap="round">
    <path d="M258 632 L322 696 M328 632 L264 696 M270 688 L256 702 M316 688 L330 702 M252 682 L276 706 M334 682 L310 706"/>
  </g>
  <!-- medal -->
  <g stroke="#fff" stroke-width="3" fill="none">
    <path d="M596 626 L608 656 M632 626 L620 656"/>
    <circle cx="614" cy="680" r="20"/>
    <path d="M614 670 V690 M609 672 H614"/>
  </g>
  <!-- burger -->
  <g stroke="#fff" stroke-width="3" fill="none" stroke-linejoin="round">
    <path d="M890 664 Q920 628 950 664 Z"/>
    <path d="M888 674 H952"/>
    <path d="M890 684 Q905 678 920 684 Q935 690 950 684"/>
    <path d="M890 694 H950 V700 Q950 704 946 704 H894 Q890 704 890 700 Z"/>
  </g>
</svg>
<div class="feature" style="left:183px;top:712px;width:220px"><h3>TOURNAMENTS</h3><p>Lorem ipsum dolor sit amet con-<br>sectetuer adipiscing elit</p><div class="chev"><svg width="14" height="9" viewBox="0 0 14 9"><path d="M1 1 L7 7 L13 1" fill="none" stroke="#fff" stroke-width="2"/></svg></div></div>
<div class="feature" style="left:504px;top:712px;width:220px"><h3>PRIZES</h3><p>Lorem ipsum dolor sit amet con-<br>sectetuer adipiscing elit</p><div class="chev"><svg width="14" height="9" viewBox="0 0 14 9"><path d="M1 1 L7 7 L13 1" fill="none" stroke="#fff" stroke-width="2"/></svg></div></div>
<div class="feature" style="left:810px;top:712px;width:220px"><h3>FOOD</h3><p>Lorem ipsum dolor sit amet con-<br>sectetuer adipiscing elit</p><div class="chev"><svg width="14" height="9" viewBox="0 0 14 9"><path d="M1 1 L7 7 L13 1" fill="none" stroke="#fff" stroke-width="2"/></svg></div></div>

<!-- who we are -->
<div class="photo" role="img" aria-label="Armoured sci-fi soldier character leaping" style="left:60px;top:990px;width:490px;height:460px;border-radius:45% 40% 30% 40%;background:radial-gradient(ellipse at 55% 45%,#4a4f8e,#2a2d5c 60%,rgba(42,45,92,0) 75%)"></div>
<h2 class="section-title abs" style="left:612px;top:1072px">WHO WE ARE</h2>
<p class="body-copy abs" style="left:612px;top:1134px;width:450px">Lorem ipsum dolor sit amet, consectetur adipiscing elit. Do-lores quae porro consequatur aliquam, incidunt eius magni provident, doloribus omnis minus ovident, doloribus Dolores quae porro consequatur aliquam, incidunt eius magni provident, doloribus omnis minus ovident Consectetur adipiscing elit. Dolores quae por</p>
<a class="btn-outline" style="left:612px;top:1313px;width:153px;height:44px" href="#">LEARN MORE</a>

<!-- tournaments -->
<h2 class="heading abs" style="left:0;width:1200px;top:1510px;text-align:center;font-size:32px;color:#fff">TOURNAMENTS</h2>
<div class="leader-row" style="top:1579px"><span class="rank">1.</span><span class="game">GAME TITLE HERE</span><span class="score"><svg class="frame" width="136" height="42" viewBox="0 0 136 42"><path d="M14 1 H135 L122 41 H1Z" fill="none" stroke="#9aa6ff" stroke-width="1.5"/></svg><svg width="18" height="16" viewBox="0 0 18 16"><circle cx="9" cy="8" r="7" fill="#fff"/></svg>13,020</span><span class="go"><svg width="18" height="16" viewBox="0 0 18 16"><path d="M1 8 H15 M9 2 L15 8 L9 14" fill="none" stroke="#fff" stroke-width="2.6"/></svg></span></div>
<div class="leader-row" style="top:1648px"><span class="rank">2.</span><span class="game">GAME TITLE HERE</span><span class="score"><svg class="frame" width="136" height="42" viewBox="0 0 136 42"><path d="M14 1 H135 L122 41 H1Z" fill="none" stroke="#9aa6ff" stroke-width="1.5"/></svg><svg width="18" height="16" viewBox="0 0 18 16"><circle cx="9" cy="8" r="7" fill="#fff"/></svg>13,020</span><span class="go"><svg width="18" height="16" viewBox="0 0 18 16"><path d="M1 8 H15 M9 2 L15 8 L9 14" fill="none" stroke="#fff" stroke-width="2.6"/></svg></span></div>
<div class="leader-row" style="top:1717px"><span class="rank">3.</span><span class="game">GAME TITLE HERE</span><span class="score"><svg class="frame" width="136" height="42" viewBox="0 0 136 42"><path d="M14 1 H135 L122 41 H1Z" fill="none" stroke="#9aa6ff" stroke-width="1.5"/></svg><svg width="18" height="16" viewBox="0 0 18 16"><circle cx="9" cy="8" r="7" fill="#fff"/></svg>13,020</span><span class="go"><svg width="18" height="16" viewBox="0 0 18 16"><path d="M1 8 H15 M9 2 L15 8 L9 14" fill="none" stroke="#fff" stroke-width="2.6"/></svg></span></div>
<div class="leader-row" style="top:1786px"><span class="rank">4.</span><span class="game">GAME TITLE HERE</span><span class="score"><svg class="frame" width="136" height="42" viewBox="0 0 136 42"><path d="M14 1 H135 L122 41 H1Z" fill="none" stroke="#9aa6ff" stroke-width="1.5"/></svg><svg width="18" height="16" viewBox="0 0 18 16"><circle cx="9" cy="8" r="7" fill="#fff"/></svg>13,020</span><span class="go"><svg width="18" height="16" viewBox="0 0 18 16"><path d="M1 8 H15 M9 2 L15 8 L9 14" fill="none" stroke="#fff" stroke-width="2.6"/></svg></span></div>
<div class="leader-row" style="top:1855px"><span class="rank">5.</span><span class="game">GAME TITLE HERE</span><span class="score"><svg class="frame" width="136" height="42" viewBox="0 0 136 42"><path d="M14 1 H135 L122 41 H1Z" fill="none" stroke="#9aa6ff" stroke-width="1.5"/></svg><svg width="18" height="16" viewBox="0 0 18 16"><circle cx="9" cy="8" r="7" fill="#fff"/></svg>13,020</span><span class="go"><svg width="18" height="16" viewBox="0 0 18 16"><path d="M1 8 H15 M9 2 L15 8 L9 14" fill="none" stroke="#fff" stroke-width="2.6"/></svg></span></div>

<!-- our games -->
<h2 class="section-title abs" style="left:0;width:1200px;top:2052px;text-align:center;font-size:32px">OUR GAMES</h2>
<div class="game-cover" role="img" aria-label="Game cover art with cartoon heroes" style="left:168px;top:2119px;background:radial-gradient(circle at 50% 40%,#6fb6e8,#2b5f9c)"></div>
<div class="game-cover" role="img" aria-label="Game cover art with armoured squad" style="left:392px;top:2119px;background:radial-gradient(circle at 50% 40%,#c9a58a,#7a5a4a)"></div>
<div class="game-cover" role="img" aria-label="Card game cover art in a tavern" style="left:611px;top:2119px;background:radial-gradient(circle at 50% 45%,#c28a3a,#4a2a18)"></div>
<div class="game-cover" role="img" aria-label="Fantasy strategy game cover art" style="left:835px;top:2119px;background:radial-gradient(circle at 50% 50%,#1f5a6a,#0a1a24)"></div>
<svg class="arrow" style="left:104px;top:2197px" width="26" height="50" viewBox="0 0 26 50"><path d="M24 2 L3 25 L24 48" fill="none" stroke="#7a78a0" stroke-width="2"/></svg>
<svg class="arrow" style="left:1070px;top:2197px" width="26" height="50" viewBox="0 0 26 50"><path d="M2 2 L23 25 L2 48" fill="none" stroke="#7a78a0" stroke-width="2"/></svg>

<!-- pricing -->
<h2 class="heading abs" style="left:0;width:1200px;top:2502px;text-align:center;font-size:32px;color:#fff">OUR PRICING</h2>

<div class="plan" style="left:161px">
  <svg class="plan-head" viewBox="0 0 280 130" preserveAspectRatio="none"><defs><linearGradient id="headA" x1="0" y1="0" x2="0" y2="1"><stop offset="0" stop-color="#3a18d8"/><stop offset="1" stop-color="#5a2ae0"/></linearGradient></defs><path d="M0 0 H280 V118 Q240 104 200 112 Q140 126 90 110 Q40 96 0 112Z" fill="url(#headA)"/></svg>
  <div class="plan-name">STANDARD</div>
  <div class="plan-price"><b>£5</b>/Per Hour</div>
  <p class="plan-desc">Lorem ipsum proin gravida nibh vel velit auctor aliquet. Aeneans ollicitudin, lorem quis</p>
  <ul class="plan-list">
    <li><svg width="15" height="15" viewBox="0 0 15 15"><circle cx="7.5" cy="7.5" r="6.5" fill="none" stroke="#8f8cf0" stroke-width="1.3"/><path d="M4.5 7.6 L6.8 9.8 L10.6 5.4" fill="none" stroke="#8f8cf0" stroke-width="1.3"/></svg>Entrance</li>
    <li><svg width="15" height="15" viewBox="0 0 15 15"><circle cx="7.5" cy="7.5" r="6.5" fill="none" stroke="#8f8cf0" stroke-width="1.3"/><path d="M4.5 7.6 L6.8 9.8 L10.6 5.4" fill="none" stroke="#8f8cf0" stroke-width="1.3"/></svg>Lunch &amp; Snacks</li>
    <li><svg width="15" height="15" viewBox="0 0 15 15"><circle cx="7.5" cy="7.5" r="6.5" fill="none" stroke="#8f8cf0" stroke-width="1.3"/><path d="M4.5 7.6 L6.8 9.8 L10.6 5.4" fill="none" stroke="#8f8cf0" stroke-width="1.3"/></svg>Custom Badge</li>
    <li><svg width="15" height="15" viewBox="0 0 15 15"><circle cx="7.5" cy="7.5" r="6.5" fill="none" stroke="#8f8cf0" stroke-width="1.3"/><path d="M4.5 7.6 L6.8 9.8 L10.6 5.4" fill="none" stroke="#8f8cf0" stroke-width="1.3"/></svg>Certificate</li>
  </ul>
  <a class="btn-outline light plan-btn" href="#">GET A QUOTE</a>
</div>

<div class="plan" style="left:462px">
  <svg class="plan-head" viewBox="0 0 280 130" preserveAspectRatio="none"><path d="M0 0 H280 V118 Q240 104 200 112 Q140 126 90 110 Q40 96 0 112Z" fill="url(#headA)"/></svg>
  <div class="plan-name">STANDARD</div>
  <div class="plan-price"><b>£7</b>/Per Hour</div>
  <p class="plan-desc">Lorem ipsum proin gravida nibh vel velit auctor aliquet. Aeneans ollicitudin, lorem quis</p>
  <ul class="plan-list">
    <li><svg width="15" height="15" viewBox="0 0 15 15"><circle cx="7.5" cy="7.5" r="6.5" fill="none" stroke="#8f8cf0" stroke-width="1.3"/><path d="M4.5 7.6 L6.8 9.8 L10.6 5.4" fill="none" stroke="#8f8cf0" stroke-width="1.3"/></svg>Entrance</li>
    <li><svg width="15" height="15" viewBox="0 0 15 15"><circle cx="7.5" cy="7.5" r="6.5" fill="none" stroke="#8f8cf0" stroke-width="1.3"/><path d="M4.5 7.6 L6.8 9.8 L10.6 5.4" fill="none" stroke="#8f8cf0" stroke-width="1.3"/></svg>Lunch &amp; Snacks</li>
    <li><svg width="15" height="15" viewBox="0 0 15 15"><circle cx="7.5" cy="7.5" r="6.5" fill="none" stroke="#8f8cf0" stroke-width="1.3"/><path d="M4.5 7.6 L6.8 9.8 L10.6 5.4" fill="none" stroke="#8f8cf0" stroke-width="1.3"/></svg>Custom Badge</li>
    <li><svg width="15" height="15" viewBox="0 0 15 15"><circle cx="7.5" cy="7.5" r="6.5" fill="none" stroke="#8f8cf0" stroke-width="1.3"/><path d="M4.5 7.6 L6.8 9.8 L10.6 5.4" fill="none" stroke="#8f8cf0" stroke-width="1.3"/></svg>Certificate</li>
  </ul>
  <a class="btn-outline light plan-btn" href="#">GET A QUOTE</a>
</div>

<div class="plan" style="left:762px">
  <svg class="plan-head" viewBox="0 0 280 130" preserveAspectRatio="none"><path d="M0 0 H280 V118 Q240 104 200 112 Q140 126 90 110 Q40 96 0 112Z" fill="url(#headA)"/></svg>
  <div class="plan-name">STANDARD</div>
  <div class="plan-price"><b>£30</b>/Per Hour</div>
  <p class="plan-desc">Lorem ipsum proin gravida nibh vel velit auctor aliquet. Aeneans ollicitudin, lorem quis</p>
  <ul class="plan-list">
    <li><svg width="15" height="15" viewBox="0 0 15 15"><circle cx="7.5" cy="7.5" r="6.5" fill="none" stroke="#8f8cf0" stroke-width="1.3"/><path d="M4.5 7.6 L6.8 9.8 L10.6 5.4" fill="none" stroke="#8f8cf0" stroke-width="1.3"/></svg>Entrance</li>
    <li><svg width="15" height="15" viewBox="0 0 15 15"><circle cx="7.5" cy="7.5" r="6.5" fill="none" stroke="#8f8cf0" stroke-width="1.3"/><path d="M4.5 7.6 L6.8 9.8 L10.6 5.4" fill="none" stroke="#8f8cf0" stroke-width="1.3"/></svg>Lunch &amp; Snacks</li>
    <li><svg width="15" height="15" viewBox="0 0 15 15"><circle cx="7.5" cy="7.5" r="6.5" fill="none" stroke="#8f8cf0" stroke-width="1.3"/><path d="M4.5 7.6 L6.8 9.8 L10.6 5.4" fill="none" stroke="#8f8cf0" stroke-width="1.3"/></svg>Custom Badge</li>
    <li><svg width="15" height="15" viewBox="0 0 15 15"><circle cx="7.5" cy="7.5" r="6.5" fill="none" stroke="#8f8cf0" stroke-width="1.3"/><path d="M4.5 7.6 L6.8 9.8 L10.6 5.4" fill="none" stroke="#8f8cf0" stroke-width="1.3"/></svg>Certificate</li>
  </ul>
  <a class="btn-outline light plan-btn" href="#">GET A QUOTE</a>
</div>

<!-- food -->
<div class="photo" role="img" aria-label="Burger, fries and a soft drink" style="left:201px;top:3105px;width:312px;height:357px;border-radius:40%;background:radial-gradient(ellipse at 50% 60%,#e0a04a,#c8452e 45%,rgba(255,255,255,0) 72%)"></div>
<h2 class="section-title abs" style="left:584px;top:3164px">FOOD</h2>
<p class="body-copy abs" style="left:584px;top:3226px;width:450px">Lorem ipsum dolor sit amet, consectetur adipiscing elit. Do-lores quae porro consequatur aliquam, incidunt eius magni provident, doloribus omnis minus ovident, doloribus Dolores quae porro consequatur aliquam, incidunt eius magni provident, doloribus omnis minus</p>
<a class="btn-outline" style="left:584px;top:3382px;width:154px;height:43px" href="#">LEARN MORE</a>

<!-- prizes -->
<h2 class="heading abs" style="left:183px;top:3634px;font-size:33px;color:#fff">PRIZES</h2>
<p class="body-copy abs" style="left:183px;top:3694px;width:420px;color:#e6e3ff">Lorem ipsum dolor sit amet, consectetur adipiscing elit. Dolores quae porro consequatur aliquam, incidunt eius magni provident, doloribus omnis<br>Dolores quae porro consequatur aliquam, incidunt eius magni provident, doloribus omnis minus</p>
<a class="btn-outline light" style="left:183px;top:3849px;width:154px;height:44px" href="#">LEARN MORE</a>
<div class="photo" role="img" aria-label="Wooden barrels and chest overflowing with gold coins" style="left:650px;top:3572px;width:376px;height:367px;border-radius:40%;background:radial-gradient(ellipse at 50% 45%,#f0c23a,#9a5a20 45%,rgba(42,23,110,0) 72%)"></div>

<!-- contact -->
<h2 class="section-title abs" style="left:0;width:1200px;top:4066px;text-align:center;font-size:32px">CONTACT FORM</h2>
<div class="field" style="left:185px;top:4137px;width:410px;height:46px">Name</div>
<div class="field" style="left:185px;top:4192px;width:410px;height:46px">Email</div>
<div class="field" style="left:185px;top:4246px;width:410px;height:46px">Phone</div>
<div class="field" style="left:604px;top:4137px;width:407px;height:155px">Message</div>
<a class="btn-outline submit" href="#">SUBMIT NOW</a>

<!-- footer -->
<div class="hours">OPENING HOURS: MON TO FRI: 10 AM TO 7 PM</div>
<nav class="foot-nav">
  <a href="#" style="margin-right:50px">HOME</a>
  <a href="#" style="margin-right:50px">ABOUT</a>
  <a href="#" style="margin-right:50px">GAMES</a>
  <a href="#" style="margin-right:50px">EVENTS</a>
  <a href="#" style="margin-right:50px">PRICE</a>
  <a href="#">CONTACT</a>
</nav>
<div class="copyright">© 2019 Company Name. All right reserved</div>
<a class="social" style="left:493px" href="#" aria-label="Social link 1"></a>
<a class="social" style="left:548px" href="#" aria-label="Social link 2"></a>
<a class="social" style="left:603px" href="#" aria-label="Social link 3"></a>
<a class="social" style="left:658px" href="#" aria-label="Social link 4"></a>

</body>
</html>
```